Company or website name
- Resume for accounting
- Links to the website
- http://www.ventanaslumbre.com/#portada
- Describe your company and organization and target audience
- The web layout is not for a business. This is a personal site that will present my CV. I am an accountant. It would be nice to follow a model like this website: http://www.ventanaslumbre.com/#portada . The main users of the site will be recruiters.
- The design should have the following
- The design must be modern . There must be both personal photos and scenes work as an office and buildings.

```html
<!DOCTYPE html>
<html lang="en">
<head>
<meta charset="utf-8">
<title>Accountant Resume — Highlights</title>
<link rel="stylesheet" href="https://fonts.googleapis.com/css2?family=PT+Serif:ital,wght@1,400;1,700&display=swap">
<style>
  :root {
    --bg: #000000;
    --text: #f2f2f2;
    --nav-text: #e6e6e6;
    --rail-light: #5a5a5a;
    --photo-mid: #3a3a3a;
    --photo-dark: #0c0c0c;
  }
  html, body {
    margin: 0;
    padding: 0;
    width: 1200px;
    height: 675px;
    overflow: hidden;
    background: var(--bg);
  }
  .page {
    position: relative;
    width: 1200px;
    height: 675px;
    background: var(--bg);
    font-family: "PT Serif", Georgia, serif;
    font-style: italic;
    color: var(--text);
  }
  .side-rail {
    position: absolute;
    left: 43px;
    top: 0;
    width: 5px;
    height: 660px;
    background: linear-gradient(to bottom, transparent 0%, var(--rail-light) 40%, var(--rail-light) 60%, transparent 100%);
    opacity: 0.7;
  }
  .main-nav {
    position: absolute;
    left: 55px;
    top: 137px;
    width: 140px;
    margin: 0;
    padding: 0;
    list-style: none;
    text-align: center;
  }
  .main-nav li {
    height: 26.4px;
    font-size: 13px;
    letter-spacing: 0.9px;
    color: var(--nav-text);
  }
  .main-nav .is-first { font-weight: 700; }
  .main-nav .is-current { text-decoration: underline; text-underline-offset: 2px; }
  .highlights {
    position: absolute;
    left: 365px;
    top: 136px;
    margin: 0;
    padding: 0;
    list-style: none;
  }
  .highlights li {
    height: 18.8px;
    font-size: 16px;
    font-weight: 700;
    letter-spacing: 1.6px;
    line-height: 18.8px;
    white-space: nowrap;
  }
  .highlights li::before { content: "· "; }
  .work-photo {
    position: absolute;
    left: 590px;
    top: 300px;
    width: 510px;
    height: 330px;
    background: radial-gradient(ellipse 50% 45% at 58% 48%, var(--photo-mid) 0%, var(--photo-dark) 60%, var(--bg) 100%);
  }
</style>
</head>
<body>
  <div class="page">
    <div class="side-rail"></div>
    <ul class="main-nav">
      <li class="is-first">SUMMARY</li>
      <li class="is-current">HIGHLITS</li>
      <li>EXPERIENCE</li>
      <li>EDUCATION</li>
      <li>CONTACT</li>
    </ul>
    <ul class="highlights">
      <li>GAAP KNOWLEDGE</li>
      <li>BUDGET FORECASTING EXPERTISE</li>
      <li>ACCOUNT RECONCILIATION EXPERT</li>
      <li>FINANCIAL STATEMENT ANALYSIS</li>
      <li>TEAM LEADERSHIP</li>
      <li style="margin-top:1.5px">GENERAL LEDGER ACCOUNTING</li>
      <li>REPORTING PROFICIENCY</li>
      <li>ANALYTICAL</li>
      <li>ORGANIZED</li>
      <li>DETAIL-ORIENTED</li>
    </ul>
    <div class="work-photo" role="img" aria-label="Dim black-and-white photo of a pen resting on a printed income statement showing operating expenses and pre-tax profit"></div>
  </div>
</body>
</html>
```